Lumbite Site

I would like to do a blog for food lovers. The name of the blog is BiteLum. I want to build something like Corbin Maddox and Elric Vantreau. Something cool and different. In this blog i need: Place for pictures, videos, snapvista connection, Linkwave Linked to see fans wich like the blog on Linkwave....

Reason: I need more options of design.

Build

Requirements
Nice to have
• - Linkwave link
- Snapvista
- Something with tripnook

```html
<!DOCTYPE html>
<html lang="en">
<head>
<meta charset="utf-8">
<title>Lumbite — Food Blog</title>
<link rel="stylesheet" href="https://fonts.googleapis.com/css2?family=Open+Sans:ital,wght@0,300;0,400;0,600;1,400&family=Noto+Serif:ital@1&display=swap">
<style>
:root{
  --ink:#222;
  --text:#4a4a4a;
  --muted:#8a8a8a;
  --page:#e6e6e6;
  --panel:#ffffff;
  --dark:#1d1d1d;
  --dark-2:#2a2a2a;
  --yellow:#f5c400;
  --orange:#e8801a;
  --blue:#2fa3c9;
  --rule:#e2e2e2;
  --share:#5a74a8;
}
*{box-sizing:border-box;margin:0;padding:0}
html,body{width:1200px;height:2432px;overflow:hidden}
body{background:var(--page);font-family:"Open Sans",Arial,sans-serif;color:var(--text);position:relative}
.abs{position:absolute}

/* header */
.masthead{left:0;top:0;width:1200px;height:260px;background:repeating-linear-gradient(90deg,#1a1a1a 0 3px,#232323 3px 6px)}
.masthead-photo{left:150px;top:0;width:900px;height:235px;background:radial-gradient(ellipse at 25% 60%,#c8182a 0,#8e1020 45%,transparent 70%),radial-gradient(ellipse at 78% 50%,#b3202a 0,#6d0f18 50%,transparent 75%),linear-gradient(180deg,#3a0b10,#7a1420 60%,#2a0a0c);border-radius:0 0 10px 10px}
.logo-badge{left:498px;top:10px;width:204px;height:204px;border-radius:50%;background:#fff;border:6px solid #e9e9e9;box-shadow:0 4px 10px rgba(0,0,0,.35)}
.logo-name{left:498px;top:82px;width:204px;text-align:center;font-weight:300;font-size:38px;color:#8d8d8d;letter-spacing:1px}

/* content panel */
.panel{left:142px;top:240px;width:916px;height:1778px;background:var(--panel);box-shadow:0 6px 14px rgba(0,0,0,.18)}
.welcome{left:142px;top:240px;width:916px;height:76px;background:#f0f0f0;border-bottom:8px solid #dcdcdc}
.welcome h1{position:absolute;left:22px;top:18px;font-family:"Noto Serif",Georgia,serif;font-style:italic;font-weight:400;font-size:30px;color:#8a8a8a}
.welcome h1 em{color:var(--blue)}
.social{position:absolute;top:20px;width:30px;height:30px;border-radius:50%;background:#c9c9c9}

/* posts */
.post-flag{width:44px;height:44px;background:var(--yellow);clip-path:polygon(0 0,78% 0,100% 50%,78% 100%,0 100%);left:130px}
.post-flag svg{position:absolute;left:10px;top:12px}
.post-title{left:200px;font-size:22px;font-weight:400;color:var(--ink);letter-spacing:1px}
.post-media{left:162px;width:568px;border:5px solid #ddd;background:linear-gradient(135deg,#5a8a2a,#c0392b 35%,#e0a020 60%,#3f7a26)}
.post-media.video{background:linear-gradient(180deg,#7aa6c8,#4d7a5a 55%,#2b3a20)}
.post-body{left:162px;width:568px;font-size:12.3px;line-height:19px;color:var(--text)}
.post-body p+p{margin-top:18px}
.post-meta{left:162px;width:568px;height:26px;border-top:1px solid var(--rule);padding-top:6px;font-size:12.5px}
.more{position:absolute;left:0;top:8px;color:var(--orange)}
.comments{position:absolute;left:296px;top:8px;color:#555}
.btn{position:absolute;top:7px;height:16px;font-size:10px;line-height:16px;padding:0 6px;color:#fff;border-radius:2px}
.btn.share{left:390px;background:var(--share)}
.btn.post{left:490px;background:#d9ecf7;color:#2f6f99;border:1px solid #a9cbe0;line-height:14px}
.count{position:absolute;top:7px;height:16px;font-size:10px;line-height:14px;padding:0 5px;border:1px solid #ccc;color:#555;background:#fff}
.post-rule{left:162px;width:568px;height:8px;background:#ececec}
.player{left:167px;width:558px;height:22px;background:#e9e9e9;border-top:1px solid #ccc}

/* sidebar */
.side-title{left:758px;font-size:19px;color:var(--ink)}
.side-title span{color:var(--orange)}
.search{left:762px;top:369px;width:278px;height:32px;border:3px solid var(--yellow);border-radius:16px;background:#fff;font-size:12px;color:#777;padding:6px 0 0 34px}
.side-rule{left:758px;width:282px;height:6px;background:#ececec}
.side-video{left:758px;top:490px;width:282px;height:224px;border:5px solid #ddd;background:linear-gradient(135deg,#d7b98a,#c45a3a 55%,#6a8a4a)}
.play{left:876px;top:580px;width:34px;height:26px;background:#d21f1f;border-radius:5px}
.grid{left:758px;top:813px;width:282px;display:grid;grid-template-columns:repeat(4,64px);gap:8px}
.grid div{height:65px;border:3px solid #ddd;background:linear-gradient(160deg,#e3c4a8,#9a6f52)}

/* pagination */
.pager{left:428px;top:2043px;display:flex;gap:4px;font-size:11px}
.pager span{min-width:20px;height:22px;line-height:20px;text-align:center;border:1px solid #bbb;background:#fff;color:#333;padding:0 4px}
.pager .on{background:var(--yellow);border-color:#d6a800}

/* footer */
.footer{left:0;top:2102px;width:1200px;height:330px;background:repeating-linear-gradient(90deg,var(--dark) 0 3px,var(--dark-2) 3px 6px)}
.foot-icon{width:36px;height:36px;border-radius:50%;background:var(--yellow)}
.foot-head{font-size:17px;color:#fff}
.foot-text{font-size:12.5px;line-height:19px;color:#6e6e6e}
.foot-date{font-size:12px;font-style:italic;color:var(--yellow)}
.thumb{width:58px;height:58px;border:3px solid #eee;background:linear-gradient(160deg,#f0d2a8,#b8875e)}
.quote{left:492px;top:2200px;width:276px;height:120px;border-bottom:1px solid #555;font-size:12.5px;line-height:19px;color:#6e6e6e;padding-left:14px}
.copy{left:142px;top:2402px;font-size:11.5px;color:#666}
.foot-social{top:2400px;width:20px;height:20px;border-radius:50%;background:#444}
</style>
</head>
<body>

<header>
  <div class="abs masthead"></div>
  <div class="abs masthead-photo" role="img" aria-label="Close-up photo of red apples and strawberries"></div>
  <div class="abs logo-badge"></div>
  <div class="abs logo-name">Lumbite</div>
</header>

<main>
  <div class="abs panel"></div>
  <div class="abs welcome">
    <h1>Welcome to <em>LUMBITE</em> Blog. Enjoy!</h1>
    <span class="social" style="left:746px"></span>
    <span class="social" style="left:782px"></span>
    <span class="social" style="left:818px"></span>
    <span class="social" style="left:854px"></span>
  </div>

  <!-- Post 1 -->
  <div class="abs post-flag" style="top:334px"><svg width="22" height="18" viewBox="0 0 22 18"><rect x="1" y="4" width="20" height="13" rx="2" fill="#222"/><rect x="7" y="1" width="8" height="4" fill="#222"/><circle cx="11" cy="10.5" r="4" fill="#f5c400"/></svg></div>
  <h2 class="abs post-title" style="top:342px">THE STANDARD LOREM IPSUM PASSAGE</h2>
  <div class="abs post-media" style="top:401px;height:252px" role="img" aria-label="Photo of a market stall piled with fresh vegetables and fruit"></div>
  <div class="abs post-body" style="top:666px">
    <p>Lorem ipsum dolor sit amet, consectetur adipisicing elit, sed do eiusmod tempor incididunt ut labore et dolore magna aliqua.</p>
    <p>Ut enim ad minim veniam, quis nostrud us exercitation ullamco laboris nisi ut aliquip ex ea commodo consequat. Duis aute irure dolor intr reprehenderit in voluptate velit esserse cillum dolore eu fugiat nulla pariatur.</p>
  </div>
  <div class="abs post-meta" style="top:788px">
    <span class="more">Continue Reading →</span><span class="comments">10 comments</span>
    <span class="btn share">Share</span><span class="count" style="left:444px">37</span>
    <span class="btn post">Post</span><span class="count" style="left:540px">56</span>
  </div>
  <div class="abs post-rule" style="top:834px"></div>

  <!-- Post 2 -->
  <div class="abs post-flag" style="top:886px"><svg width="22" height="18" viewBox="0 0 22 18"><rect x="1" y="4" width="20" height="13" rx="2" fill="#222"/><rect x="7" y="1" width="8" height="4" fill="#222"/><circle cx="11" cy="10.5" r="4" fill="#f5c400"/></svg></div>
  <h2 class="abs post-title" style="top:894px">THE STANDARD LOREM IPSUM PASSAGE</h2>
  <div class="abs post-media" style="top:953px;height:252px" role="img" aria-label="Photo of a market stall piled with fresh vegetables and fruit"></div>
  <div class="abs post-body" style="top:1218px">
    <p>Lorem ipsum dolor sit amet, consectetur adipisicing elit, sed do eiusmod tempor incididunt ut labore et dolore magna aliqua.</p>
    <p>Ut enim ad minim veniam, quis nostrud us exercitation ullamco laboris nisi ut aliquip ex ea commodo consequat. Duis aute irure dolor intr reprehenderit in voluptate velit esserse cillum dolore eu fugiat nulla pariatur.</p>
  </div>
  <div class="abs post-meta" style="top:1340px">
    <span class="more">Continue Reading →</span><span class="comments">10 comments</span>
    <span class="btn share">Share</span><span class="count" style="left:444px">37</span>
    <span class="btn post">Post</span><span class="count" style="left:540px">56</span>
  </div>
  <div class="abs post-rule" style="top:1394px"></div>

  <!-- Post 3 -->
  <div class="abs post-flag" style="top:1438px"><svg width="22" height="18" viewBox="0 0 22 18"><rect x="1" y="3" width="14" height="12" rx="2" fill="#222"/><polygon points="15,9 21,4 21,14" fill="#222"/></svg></div>
  <h2 class="abs post-title" style="top:1446px">THE STANDARD LOREM IPSUM PASSAGE</h2>
  <div class="abs post-media video" style="top:1506px;height:332px" role="img" aria-label="Video still of a farmer in a hat holding a crate of vegetables in a field"></div>
  <svg class="abs" style="left:420px;top:1648px" width="50" height="50" viewBox="0 0 50 50"><circle cx="25" cy="25" r="23" fill="rgba(255,255,255,.25)" stroke="#fff" stroke-width="2"/><polygon points="20,15 36,25 20,35" fill="#fff"/></svg>
  <div class="abs player" style="top:1811px"><svg width="558" height="22" viewBox="0 0 558 22"><polygon points="8,6 16,11 8,16" fill="#333"/><rect x="34" y="9" width="370" height="4" rx="2" fill="#bbb"/><circle cx="38" cy="11" r="5" fill="#555"/><text x="430" y="15" font-size="10" fill="#555" font-family="Open Sans, sans-serif">0:00 / 0:00</text><rect x="490" y="7" width="10" height="8" fill="#444"/><rect x="530" y="6" width="16" height="10" fill="#444"/></svg></div>
  <div class="abs post-body" style="top:1852px">
    <p>Lorem ipsum dolor sit amet, consectetur adipisicing elit, sed do eiusmod tempor incididunt ut labore et dolore magna aliqua.</p>
    <p>Ut enim ad minim veniam, quis nostrud us exercitation ullamco laboris nisi ut aliquip ex ea commodo consequat. Duis aute irure dolor intr reprehenderit in voluptate velit esserse cillum dolore eu fugiat nulla pariatur.</p>
  </div>
  <div class="abs post-meta" style="top:1974px">
    <span class="more">Continue Reading →</span><span class="comments">10 comments</span>
    <span class="btn share">Share</span><span class="count" style="left:444px">37</span>
    <span class="btn post">Post</span><span class="count" style="left:540px">56</span>
  </div>

  <!-- Sidebar -->
  <aside>
    <h3 class="abs side-title" style="top:330px">Blog Search</h3>
    <div class="abs search">Enter Your Keyword...</div>
    <svg class="abs" style="left:774px;top:378px" width="14" height="14" viewBox="0 0 14 14"><circle cx="6" cy="6" r="4.5" fill="none" stroke="#777" stroke-width="2"/><line x1="9.5" y1="9.5" x2="13" y2="13" stroke="#777" stroke-width="2"/></svg>
    <div class="abs side-rule" style="top:430px"></div>

    <h3 class="abs side-title" style="top:458px">Watch <span>Our Video</span></h3>
    <div class="abs side-video" role="img" aria-label="Video still of a shopper choosing produce at a market"></div>
    <div class="abs play"><svg width="34" height="26" viewBox="0 0 34 26"><polygon points="13,7 23,13 13,19" fill="#fff"/></svg></div>

    <h3 class="abs side-title" style="top:768px">Snapvista <span>Connection</span></h3>
    <div class="abs side-rule" style="top:800px;height:4px;background:#333"></div>
    <div class="abs grid" role="img" aria-label="Grid of twelve follower portrait photos">
      <div></div><div></div><div></div><div></div>
      <div></div><div></div><div></div><div></div>
      <div></div><div></div><div></div><div></div>
    </div>
  </aside>

  <nav class="abs pager">
    <span class="on">1</span><span>2</span><span>3</span><span>4</span><span>5</span><span>6</span><span>7</span><span>8</span><span>9</span><span>...</span><span>Next &gt;</span><span>Last &gt;&gt;</span>
  </nav>
</main>

<footer>
  <div class="abs footer"></div>

  <div class="abs foot-icon" style="left:140px;top:2142px"></div>
  <h4 class="abs foot-head" style="left:186px;top:2160px">Latest News</h4>
  <div class="abs thumb" style="left:140px;top:2206px" role="img" aria-label="Portrait photo thumbnail"></div>
  <div class="abs foot-date" style="left:216px;top:2210px">15 March, 2012</div>
  <div class="abs foot-text" style="left:216px;top:2228px">Lorem ipsum dolor sit amet<br>consectetur elit...</div>
  <div class="abs thumb" style="left:140px;top:2296px" role="img" aria-label="Portrait photo thumbnail"></div>
  <div class="abs foot-date" style="left:216px;top:2300px">15 March, 2012</div>
  <div class="abs foot-text" style="left:216px;top:2318px">Lorem ipsum dolor sit amet<br>consectetur elit...</div>

  <div class="abs foot-icon" style="left:490px;top:2142px"></div>
  <h4 class="abs foot-head" style="left:538px;top:2160px">Client's Speak</h4>
  <div class="abs quote"><span style="position:absolute;left:0;top:-4px;font-size:22px;color:#999">“</span>Lorem ipsum dolor sit amet, consectetuer adipiscing elit, sed diam nonummy nibh euismod tincidunttsed diam nonummy nibh euismod tincidunt ut laoreet dolore magna aliquam erat volutpat Ut wisi enim.</div>
  <div class="abs foot-date" style="left:686px;top:2346px">MARA QUILLON</div>

  <div class="abs foot-icon" style="left:888px;top:2142px"></div>
  <h4 class="abs foot-head" style="left:934px;top:2160px">Contact Us</h4>
  <div class="abs foot-text" style="left:888px;top:2196px">Lorem ipsum dolor sit amet,<br>Consectetuer adipiscing elit,<br>Laoreet dolore magna.</div>
  <svg class="abs" style="left:888px;top:2276px" width="14" height="14" viewBox="0 0 14 14"><path d="M3 1l3 3-2 2c1 2 2 3 4 4l2-2 3 3-2 2C5 12 2 9 1 3z" fill="#999"/></svg>
  <div class="abs foot-text" style="left:914px;top:2272px;color:var(--yellow)">555 013 2846</div>
  <svg class="abs" style="left:888px;top:2302px" width="14" height="10" viewBox="0 0 14 10"><rect width="14" height="10" fill="#999"/><polyline points="0,0 7,6 14,0" fill="none" stroke="#333"/></svg>
  <div class="abs foot-text" style="left:914px;top:2296px;color:var(--yellow)">info@lumbite.com</div>

  <div class="abs copy">Copyright©2012 Lumbite. All Rights Reserved.</div>
  <span class="abs foot-social" style="left:958px"></span>
  <span class="abs foot-social" style="left:984px"></span>
  <span class="abs foot-social" style="left:1010px"></span>
  <span class="abs foot-social" style="left:1036px"></span>
</footer>

</body>
</html>
```